Radiant Crossing - An Exciting Mission & Book Cover Project

Help me to inspire people to live their best life! This is a mission, not just a design project.
I need a Book Cover designed to keep me inspired on the process of writing my book.
Book Title: Radiant Crossing
Tag Line: Three Simple Steps to get out of your own way, SuperCharge your Life and Step into Purpose!
Author: Marlis Quenby

The three steps are: Ownership, Vision and Action (Not sure if this should be on the front or back of the book cover)

The book is a self-help, motivational book. Personal development.
The cover needs to be strong and capture peoples attention, especially with competing shelf space. I almost see a fire ball of flame or explosion that will grab peoples attention.
My company is The Lantern Institute. I have added the company logo and a few pages of my presentation and topic outline to give an idea.
Maybe: The Lantern Institute logo on back of the cover. website is marlisquenby.com

THOUGHT: People should be able to take a photo of them holding the book cover showing what area of life they want Radiant Crossing in. This is why the front cover must be so visual and powerful that they want to take a photo with it. Ie. Explosion, fire, strong and bold.

Target Market(s)

Anyone who feels stuck and needs to breakthrough and move forward in life.

Industry/Entity Type

Motivation

Font styles to use
Serif
Sans Serif

Colors
ec1f27
f37122
fbed22

Requirements
Must have
• The design must be STRONG, SIMPLE, STAND OUT ON BOOK SHELVES.
Must have an open file to swap the photo and copy out.

Back Cover Page
1) Summary
2) 2-3 testimonials. One sentence.
3) About the Author (maybe with photo)
4) Lantern Institute logo
5) Website: radiantcrossing.com and marlisquenby.com
Nice to have
• If my photo works somewhere that would be great. I will change the photo later.
Added Where's Your Harbor? a nice cover example.
Should not have
• Right now I am writing the summary for the back of the cover. For now use Loreum Ipsum text and 2-3 recommendations. Again, I will get these only later.

```html
<!DOCTYPE html>
<html lang="en">
<head>
<meta charset="utf-8">
<title>Radiant Crossing – Book Cover</title>
<link rel="stylesheet" href="https://fonts.googleapis.com/css2?family=Fira+Sans:wght@700&family=Fira+Sans+Condensed:wght@400;600;700&display=swap">
<style>
  :root {
    --page-bg: #ffffff;
    --cover-black: #070302;
    --ember-deep: #3a1205;
    --ember-mid: #a8420d;
    --ember-bright: #f37122;
    --flame-glow: #fbb45a;
    --title-red: #ec1f27;
    --title-white: #ffffff;
  }
  html, body {
    margin: 0;
    padding: 0;
    width: 1113px;
    height: 1200px;
    overflow: hidden;
    background: var(--page-bg);
  }
  .book-cover {
    position: absolute;
    left: 176px;
    top: 30px;
    width: 760px;
    height: 1140px;
    background: var(--cover-black);
    overflow: hidden;
    color: var(--title-white);
    text-align: center;
  }
  .cover-art {
    position: absolute;
    left: 0;
    top: 300px;
    width: 760px;
    height: 840px;
    background:
      radial-gradient(ellipse 32% 40% at 50% 55%, #000000 0%, #0a0402 70%, rgba(10,4,2,0) 100%),
      radial-gradient(ellipse 70% 60% at 50% 45%, var(--flame-glow) 0%, var(--ember-bright) 30%, var(--ember-mid) 55%, var(--ember-deep) 78%, var(--cover-black) 100%);
  }
  .cover-glow-top {
    position: absolute;
    left: 0;
    top: 0;
    width: 760px;
    height: 420px;
    background: radial-gradient(ellipse 60% 55% at 50% 95%, rgba(120,45,10,0.55) 0%, rgba(7,3,2,0) 100%);
  }
  .title-primary {
    position: absolute;
    left: 0;
    right: 0;
    top: 22px;
    margin: 0;
    font-family: "Fira Sans", sans-serif;
    font-weight: 700;
    font-size: 150px;
    line-height: 1;
    letter-spacing: -3px;
    color: var(--title-red);
  }
  .title-secondary {
    position: absolute;
    left: 0;
    right: 0;
    top: 168px;
    margin: 0;
    font-family: "Fira Sans", sans-serif;
    font-weight: 700;
    font-size: 112px;
    line-height: 1;
    letter-spacing: -2px;
    color: var(--title-white);
  }
  .subtitle {
    position: absolute;
    left: 0;
    right: 0;
    top: 282px;
    margin: 0;
    font-family: "Fira Sans Condensed", sans-serif;
    font-weight: 400;
    font-size: 39px;
    line-height: 1;
    color: var(--title-white);
  }
  .tagline {
    position: absolute;
    left: 180px;
    width: 400px;
    top: 680px;
    margin: 0;
    font-family: "Fira Sans Condensed", sans-serif;
    font-weight: 600;
    font-size: 32px;
    line-height: 42px;
    color: var(--title-white);
  }
  .author {
    position: absolute;
    left: 0;
    right: 0;
    top: 1078px;
    margin: 0;
    font-family: "Fira Sans Condensed", sans-serif;
    font-size: 42px;
    line-height: 1;
    text-transform: uppercase;
    color: var(--title-white);
  }
  .author-first { font-weight: 700; }
  .author-last { font-weight: 400; }
</style>
</head>
<body>
  <main class="book-cover">
    <div class="cover-glow-top"></div>
    <div class="cover-art" role="img" aria-label="Silhouette of a muscular figure engulfed in bright orange flames on a black background"></div>
    <h1 class="title-primary">Radiant</h1>
    <h2 class="title-secondary">Crossing</h2>
    <p class="subtitle">Rapid Life Transformation</p>
    <p class="tagline">Three Simple Steps<br>to get out<br>of your own way,<br>SuperCharge<br>your Life<br>and<br>Step into<br>Purpose!</p>
    <p class="author"><span class="author-first">Marlis</span> <span class="author-last">Quenby</span></p>
  </main>
</body>
</html>
```